NCCS Brochure Design

Northern Council of Clinical Standards (NCCS) needs a whole new brochure. I've upload EPS logos and past brochures. Our tagline is to "modernize healthcare" and we think our brochure should reflect that, so that's the purpose of this project.

NCCS is a proven leader in healthcare education, training and
consulting services for health professionals. We’ve earned a reputation for excellence in healthcare quality improvement and management.

NCCS works to improve healthcare quality by educating healthcare professionals about healthcare best practices. We focus on instructing our clients on how to plan for, measure, and improve healthcare quality in all facilities and facets such as:

Patient Safety
Infection Control
Performance Improvement
Risk Management
Compliance and Accreditation
Health and Hospital Administration
Health Insurance
Healthcare Financial Management
Facility Management and Safety

DESIGN SUGGESTIONS:

Brochure Size: 8.5 X 11 full size brochure or 8.5 X 11 trifold brochure

Number of Pages: 2 to 3

Colors: Feel free to use a wide array of colors but try to stay away from colors that are too loud, ex: Pink, Purple, Neon Green.

Themes: Professional, Educational

Designs:

Povel by Tobias Lindqvist

Corvane Leaflet by Derek Halloway

Means for assembly by Quentaro

Figura de Sr KB by vrpl

http://www.plimbo-example.net/post/48210937561/10-creative-brochure-designs

Don't limit yourself to these examples. However, these are examples we liked

Reason: We would like to see more designs

We want more full page designs than tri-fold 

We are considering both tri-fold and full-page but would like to see more full page designs 

Reason: Our lead designer making the decisions on this project has been fired. I apologize for the inconvenience. We want extend the project one last time

Target Market(s)

Students, Doctors, and Educational Professionals

Industry/Entity Type

Healthcare

Logo Text

asdfasdf

Font styles to use
Serif
Sans Serif
Decorative
Script

Requirements
Should not have
• Pink, Purple, Neon Green colors

```html
<!DOCTYPE html>
<html lang="en">
<head>
<meta charset="utf-8">
<title>NCCS Brochure – Front Panel</title>
<link href="https://fonts.googleapis.com/css2?family=Arimo:ital,wght@0,400;0,700;1,700&display=swap" rel="stylesheet">
<style>
  :root {
    --backdrop: #e4e6e3;
    --paper: #ffffff;
    --paper-shade: #eeeeef;
    --navy: #1f2f66;
    --navy-light: #34467f;
    --sky: #5fb8dc;
    --sky-soft: #8fcde6;
    --photo-light: #f3f5f7;
    --photo-mid: #dde6ee;
    --text-light: #f2f4f8;
  }
  * { margin: 0; padding: 0; box-sizing: border-box; }
  html, body {
    width: 1200px; height: 806px; overflow: hidden;
    background: var(--backdrop);
    font-family: "Arimo", Arial, sans-serif;
  }
  .canvas { position: relative; width: 1200px; height: 806px; }
  .panel {
    position: absolute; left: 390px; top: 23px;
    width: 420px; height: 760px;
    background: var(--paper);
    overflow: hidden;
    box-shadow: 0 6px 18px rgba(0,0,0,0.12);
  }
  .photo {
    position: absolute; left: 0; top: 0; width: 420px; height: 420px;
    background: linear-gradient(160deg, var(--photo-light) 0%, var(--photo-mid) 55%, #c9dbe8 100%);
  }
  .header {
    position: absolute; left: 0; top: 0; width: 420px; height: 128px;
    background: linear-gradient(180deg, rgba(255,255,255,0.95) 70%, rgba(255,255,255,0));
  }
  .logo {
    position: absolute; left: 26px; top: 30px;
    display: flex; align-items: center; gap: 12px;
  }
  .logo-mark {
    width: 54px; height: 54px; border-radius: 50%;
    background: var(--navy);
  }
  .logo-name {
    font-weight: 700; font-size: 46px; color: var(--navy);
    letter-spacing: 2px; line-height: 1;
  }
  .logo-sub {
    position: absolute; left: 92px; top: 90px;
    font-size: 13px; color: var(--navy);
  }
  .bands { position: absolute; left: 0; top: 0; }
  .tagline-top {
    position: absolute; left: 24px; top: 352px;
    font-style: italic; font-weight: 700; font-size: 50px;
    color: var(--paper); transform: rotate(-9deg); transform-origin: left bottom;
  }
  .tagline-main {
    position: absolute; left: 26px; top: 418px;
    font-size: 46px; color: var(--text-light);
    transform: rotate(-9deg); transform-origin: left bottom;
  }
  .intro {
    position: absolute; left: 28px; top: 472px; width: 330px;
    font-size: 14.5px; line-height: 1.3; color: var(--text-light);
    transform: rotate(-9deg); transform-origin: left top;
  }
  .service {
    position: absolute; left: 26px; top: 676px;
    font-size: 22px; color: var(--text-light);
    transform: rotate(-9deg); transform-origin: left bottom;
  }
  .website {
    position: absolute; left: 0; bottom: 22px; width: 420px;
    text-align: center; font-size: 15px; color: var(--navy);
  }
</style>
</head>
<body>
<main class="canvas">
  <section class="panel">
    <div class="photo" role="img" aria-label="Photo of a smiling doctor with a stethoscope and clipboard, a patient blurred in the background"></div>

    <header class="header">
      <div class="logo">
        <span class="logo-mark"></span>
        <span class="logo-name">NCCS</span>
      </div>
      <p class="logo-sub">Northern Council of Clinical Standards</p>
    </header>

    <svg class="bands" width="420" height="760" viewBox="0 0 420 760" aria-hidden="true">
      <defs>
        <linearGradient id="navyFade" x1="0" y1="1" x2="1" y2="0">
          <stop offset="0" stop-color="#34467f"/>
          <stop offset="1" stop-color="#1f2f66"/>
        </linearGradient>
      </defs>
      <polygon points="0,385 420,318 420,380 0,450" fill="#5fb8dc" opacity="0.85"/>
      <polygon points="0,448 420,380 420,652 0,722" fill="url(#navyFade)"/>
      <polygon points="0,722 420,652 420,760 0,760" fill="#ffffff"/>
      <polyline points="330,350 350,350 358,330 366,372 374,312 382,350 408,350"
                fill="none" stroke="#ffffff" stroke-width="2.5" stroke-linejoin="round"/>
    </svg>

    <p class="tagline-top">Modernize</p>
    <h1 class="tagline-main">Healthcare</h1>
    <p class="intro">NCCS is a proven leader in Healthcare Education, Training and Consulting Services for Health Professionals</p>
    <p class="service">Healthcare Financial Management</p>
    <p class="website">www.nccsonline-example.org</p>
  </section>
</main>
</body>
</html>
```